Harborline Ambulatory Flyer

Need to make a flyer similar to the attached Glenmark pdfs for Harborline Ambulatory. The write up is attached or can be found at https://www.velmontcareasc.com/bronx

Requirements
Must have
• What the existing flyer has.

```html
<!DOCTYPE html>
<html lang="en">
<head>
<meta charset="utf-8">
<title>Harborline Ambulatory Surgery Center Flyer</title>
<link rel="stylesheet" href="https://fonts.googleapis.com/css2?family=Montserrat:wght@400;600&family=PT+Serif:wght@700&family=Oswald:wght@600&display=swap">
<style>
  :root {
    --bg: #d6d6d6;
    --paper: #ffffff;
    --ink: #1b1b1b;
    --blue: #2d5bb0;
    --photo-cool: #dfe3ec;
    --photo-warm: #c9d3e2;
    --map: #cfcfcf;
  }
  * { margin: 0; padding: 0; box-sizing: border-box; }
  html, body { width: 1200px; height: 1200px; overflow: hidden; background: var(--bg); }
  body { position: relative; font-family: "Montserrat", sans-serif; color: var(--ink); }

  .page { position: absolute; top: 228px; width: 522px; height: 739px; background: var(--paper); }
  .page--front { left: 75px; }
  .page--back { left: 630px; }

  .brand { position: absolute; left: 42px; top: 56px; width: 439px; text-align: center; }
  .brand__name { font-family: "Oswald", sans-serif; font-weight: 600; font-size: 27px; line-height: 39px; letter-spacing: 0.5px; color: var(--ink); text-transform: uppercase; }
  .brand__rule { position: absolute; left: 42px; top: 160px; width: 439px; height: 5px; background: var(--blue); }

  .photo { position: absolute; top: 222px; width: 225px; height: 264px; border: 1.5px solid var(--ink); border-radius: 13px; }
  .photo--desk { left: 30px; background: linear-gradient(160deg, #f2f3f7, var(--photo-cool) 70%, #b9c3d6); }
  .photo--team { left: 268px; background: linear-gradient(135deg, #9ea6b2, var(--photo-warm) 45%, #eef1f5); }

  .body { font-size: 11.8px; line-height: 13.7px; }
  .heading { font-family: "PT Serif", serif; font-weight: 700; font-size: 13.4px; line-height: 17px; color: var(--blue); text-transform: uppercase; }

  .front-intro { position: absolute; left: 47px; top: 538px; width: 425px; }
  .front-heading { position: absolute; left: 47px; top: 603px; font-size: 13px; }
  .front-location { position: absolute; left: 47px; top: 633px; width: 445px; }

  .back-block { position: absolute; left: 44px; width: 448px; }
  .cap-heading { top: 48px; }
  .cap-text { top: 98px; }
  .ben-heading { top: 256px; }
  .ben-text { top: 300px; }
  .offer-heading { top: 413px; }
  .offer-list { position: absolute; left: 44px; top: 433px; width: 470px; list-style: none; display: grid; grid-template-columns: 164px 150px 156px; }
  .offer-list li::before { content: "• "; color: var(--blue); }
  .closing { top: 482px; font-weight: 600; }

  .contact { position: absolute; left: 47px; top: 584px; font-size: 12.5px; line-height: 16px; }
  .contact p + p { margin-top: 13px; }
  .contact .web { letter-spacing: 2.6px; }
  .map { position: absolute; left: 277px; top: 562px; width: 216px; height: 149px; border-radius: 12px; background: linear-gradient(120deg, #e6e6e6, var(--map) 55%, #8a8a8a); }
</style>
</head>
<body>
  <section class="page page--front">
    <div class="brand">
      <p class="brand__name">Harborline<br>Ambulatory Surgery Center</p>
    </div>
    <div class="brand__rule"></div>

    <div class="photo photo--desk" role="img" aria-label="Photo of a doctor writing notes at a desk with a stethoscope"></div>
    <div class="photo photo--team" role="img" aria-label="Photo of a smiling medical team in white coats"></div>

    <p class="body front-intro">Harborline Ambulatory Surgery Center, is a same day surgical center, conveniently located in the Bronx,licensed by the state of New York and accredited by QSAC.</p>
    <h2 class="heading front-heading">Convenient Location for Patients and Surgeons</h2>
    <p class="body front-location">Harborline Ambulatory Surgery Center is conveniently located on Linden Avenue in the Bronx, and is easily accessed from Manhattan, Westchester and Long Island with ample parking available on site.</p>
  </section>

  <section class="page page--back">
    <h2 class="heading back-block cap-heading">Capabilities of Harborline Ambulatory<br>Surgery Center</h2>
    <p class="body back-block cap-text">Harborline Ambulatory Surgery Centeris a dedicated facility for same day procedures that do not require an overnight hospital stay, without sacrificing the quality of care and safety that a hospital provides. Withover 15,000 sq ft of space and four operating rooms, the centeroffers specialties including orthopedics, pain management, podiatry, ophthalmology, ENT, pediatric ENT, and general surgery. These same day procedures, are performed by Harborline Ambulatory Surgery Center’s highly skilled medical professionals that are committed to patient safety and satisfaction, providing the highest caliber of care with warmth and compassion in a personalized environment.</p>

    <h2 class="heading back-block ben-heading">Benefits of Chosing Harborline Ambulatory<br>Surgery Center</h2>
    <p class="body back-block ben-text">More surgeons are choosing same day surgery centers because of the ability to provide high quality care in a state-of-the-art facility, at a more reasonable cost to you, your insurance provider, and your employer. Perhaps most importantly, same day surgery requires less down time, which means you’ll spend less time away from your family and your job, and in most instances, you can return to your daily routine the next day.</p>

    <h2 class="heading back-block offer-heading">We Offer</h2>
    <ul class="body offer-list">
      <li>Orthopedics</li><li>Podiatry</li><li>Adult &amp; Pediatric ENT</li>
      <li>Pain Management</li><li>Ophthalmology</li><li>General Surgery</li>
    </ul>

    <p class="body back-block closing">Here at Harborline Ambulatory Surgery Center, the patient is our number one priority. To offer your patients the highest caliber care for same-day surgeries, contact Harborline Ambulatory Surgery Center today.</p>

    <div class="contact">
      <p>4820 Linden Ave,<br>Bronx, NY 10468</p>
      <p>Phone: (718) 555-0142<br>Email: info@velmontcareasc.com</p>
      <p class="web">www.velmontcareasc.com</p>
    </div>
    <div class="map" role="img" aria-label="Map showing the center's location in the Bronx"></div>
  </section>
</body>
</html>
```